Torvelin Business Card

We need a business card design. We have a logo from a previous PixelHarbor project and I am attaching the logo files in jpeg and photoshop.

Business

```html
<!DOCTYPE html>
<html lang="en">
<head>
<meta charset="utf-8">
<title>Torvelin Business Card</title>
<link href="https://fonts.googleapis.com/css2?family=Fira+Sans:wght@400;700&display=swap" rel="stylesheet">
<style>
  :root {
    --card-dark: #383839;
    --band-dark: #3e3e40;
    --stripe-grey: #c9c9c9;
    --brand-green: #4bb04a;
    --text-light: #ffffff;
  }
  html, body {
    margin: 0;
    padding: 0;
    width: 1200px;
    height: 720px;
    overflow: hidden;
    background: var(--card-dark);
  }
  .card {
    position: relative;
    width: 1200px;
    height: 720px;
    background: var(--card-dark);
    font-family: "Fira Sans", sans-serif;
    color: var(--text-light);
    overflow: hidden;
  }
  .brand {
    position: absolute;
    left: 160px;
    top: 212px;
    display: flex;
    align-items: center;
    gap: 26px;
  }
  .brand-mark {
    width: 56px;
    height: 56px;
    background: var(--brand-green);
  }
  .brand-name {
    font-size: 78px;
    font-weight: 700;
    line-height: 1;
    color: var(--text-light);
    margin: 0;
  }
  .contact-band {
    position: absolute;
    left: 0;
    top: 432px;
    width: 1200px;
    height: 168px;
    background: var(--band-dark);
  }
  .contact-item {
    position: absolute;
    display: flex;
    align-items: center;
    gap: 12px;
    font-size: 25px;
    line-height: 1;
    white-space: nowrap;
  }
  .contact-item svg {
    width: 22px;
    height: 26px;
    fill: var(--brand-green);
    flex: none;
  }
  .col-1 { left: 79px; }
  .col-2 { left: 463px; }
  .col-3 { left: 823px; gap: 20px; }
  .row-1 { top: 478px; }
  .row-2 { top: 542px; }
  .stripe-band {
    position: absolute;
    left: 0;
    top: 600px;
    width: 1200px;
    height: 27px;
    background: linear-gradient(to bottom, #b0b0b0 0 11px, #dedede 11px 100%);
  }
  .accent-band {
    position: absolute;
    left: 0;
    top: 627px;
    width: 1200px;
    height: 93px;
    background: var(--brand-green);
  }
</style>
</head>
<body>
<main class="card">
  <div class="brand">
    <span class="brand-mark"></span>
    <h1 class="brand-name">Torvelin</h1>
  </div>

  <section class="contact-band" aria-label="Contact details"></section>

  <div class="contact-item col-1 row-1">
    <svg viewBox="0 0 22 26" aria-hidden="true"><circle cx="11" cy="6" r="5.5"/><path d="M2 25v-7c0-4 4-6 9-6s9 2 9 6v7z"/></svg>
    <span>Name and Surname</span>
  </div>
  <div class="contact-item col-1 row-2">
    <svg viewBox="0 0 22 26" aria-hidden="true"><path d="M11 1a9 9 0 0 0-9 9c0 7 9 15 9 15s9-8 9-15a9 9 0 0 0-9-9zm0 13a4 4 0 1 1 0-8 4 4 0 0 1 0 8z"/></svg>
    <span>Address</span>
  </div>

  <div class="contact-item col-2 row-1">
    <svg viewBox="0 0 22 26" aria-hidden="true"><path d="M7 2h4l1 5-3 2c0 3 1 6 3 8l3-1 2 5-3 3C9 24 5 15 5 7z"/></svg>
    <span>Telephone</span>
  </div>
  <div class="contact-item col-2 row-2">
    <svg viewBox="0 0 22 26" aria-hidden="true"><path d="M5 2h11v8H5zM7 4v4h7V4zM1 11h20v13H1zm3 3v3h14v-3zm0 5v3h14v-3z" fill-rule="evenodd"/></svg>
    <span>Fax</span>
  </div>

  <div class="contact-item col-3 row-1">
    <svg viewBox="0 0 26 26" style="width:26px" aria-hidden="true"><circle cx="13" cy="13" r="12"/><path d="M5 8c3 0 4 2 6 2s2 3 0 4-1 4-3 5c-1-3-4-4-3-11zM16 4c2 2 5 3 6 7-2 1-3-1-5 0s-1 3-3 3c0-3-2-4 0-6s1-3 2-4z" fill="#3e3e40"/></svg>
    <span>www.yourwebsite.com</span>
  </div>
  <div class="contact-item col-3 row-2">
    <svg viewBox="0 0 24 18" style="width:24px;height:18px" aria-hidden="true"><path d="M1 1h22v16H1zm2 2v12h18V3zm0 0 9 7 9-7v2l-9 7-9-7z" fill-rule="evenodd"/></svg>
    <span>your@email.com</span>
  </div>

  <div class="stripe-band" role="img" aria-label="Grey diagonal hatched divider stripe"></div>
  <div class="accent-band"></div>
</main>
</body>
</html>
```